Nail salon window signage design

We need new signage to be designed for our existing nail salon. The sign will be a large sticker that will stick onto the glass window at the front.

Some of the services we provide are:
Manicures
Pedicures
Velora Gel Builder
Acrylic Nails
KVT
Brenlux
Gel Polish
You may wish to have our services listed on the sign but is not compulsory.

I have also attached our logo which can be used on the sign but is not compulsory.

I have also attached a photo of the front of our salon and the sign will be where I have outlined in yellow.

The size of the sign will be 119cm wide and 170cm high.

I am open to any nice classy design you can think of.

```html
<!DOCTYPE html>
<html lang="en">
<head>
<meta charset="utf-8">
<title>Aurelle Nails – Window Sign</title>
<link href="https://fonts.googleapis.com/css2?family=Montserrat:wght@800&display=swap" rel="stylesheet">
<style>
  :root {
    --wine: #8f1e33;
    --gold: #cfae74;
    --paper: #ffffff;
    --mist: #d9dadd;
  }
  * { margin: 0; padding: 0; box-sizing: border-box; }
  html, body { width: 910px; height: 1200px; overflow: hidden; background: var(--paper); }
  .sign {
    position: relative;
    width: 910px;
    height: 1200px;
    background: var(--paper);
    border: 3px solid var(--wine);
    font-family: "Montserrat", Arial, sans-serif;
  }
  .sign__texture {
    position: absolute;
    left: 0; right: 0; bottom: 0;
    height: 660px;
    background: linear-gradient(180deg, rgba(217,218,221,0) 0%, rgba(217,218,221,0.55) 45%, var(--mist) 100%);
  }
  .sign__frame {
    position: absolute;
    inset: 24px;
    border: 21px solid var(--wine);
  }
  .brand {
    position: absolute;
    top: 285px;
    left: 0; right: 0;
    text-align: center;
    color: var(--wine);
    font-weight: 800;
    font-size: 76px;
    letter-spacing: 1px;
  }
  .services {
    position: absolute;
    top: 525px;
    left: 118px;
    list-style: none;
  }
  .services__item {
    display: flex;
    align-items: center;
    height: 74px;
    color: var(--wine);
    font-weight: 800;
    font-size: 55px;
    line-height: 1;
  }
  .services__star {
    width: 58px;
    height: 58px;
    margin-right: 24px;
    flex: none;
    fill: var(--gold);
  }
</style>
</head>
<body>
  <main class="sign">
    <div class="sign__texture" role="img" aria-label="Soft grey geometric cube backdrop"></div>
    <div class="sign__frame"></div>

    <h1 class="brand">Aurelle Nails</h1>

    <svg width="0" height="0" style="position:absolute">
      <defs>
        <symbol id="star" viewBox="0 0 24 24">
          <path d="M12 1.5l3.1 7.1 7.7.7-5.8 5.1 1.7 7.6L12 18l-6.7 4 1.7-7.6L1.2 9.3l7.7-.7z"/>
        </symbol>
      </defs>
    </svg>

    <ul class="services">
      <li class="services__item"><svg class="services__star"><use href="#star"/></svg>Manicures</li>
      <li class="services__item"><svg class="services__star"><use href="#star"/></svg>Pedicures</li>
      <li class="services__item"><svg class="services__star"><use href="#star"/></svg>Velora Gel Builder</li>
      <li class="services__item"><svg class="services__star"><use href="#star"/></svg>Acrylic Nails</li>
      <li class="services__item"><svg class="services__star"><use href="#star"/></svg>KVT</li>
      <li class="services__item"><svg class="services__star"><use href="#star"/></svg>Brenlux</li>
      <li class="services__item"><svg class="services__star"><use href="#star"/></svg>Gel Polish</li>
    </ul>
  </main>
</body>
</html>
```